Restaurant service company needs a website!

I am looking for a skilled web designer/developer to create a professional, responsive, and easy-to-navigate website for my company, which specializes in servicing restaurant cooking equipment. The site should communicate trust, reliability, and technical expertise to our target audience, restaurant owners, managers, and commercial kitchen operators. I have included the company logos, if any other format for them is needed please let me know.

Target Market(s)

restaurant owners, managers, and commercial kitchen operators

Industry/Entity Type

Commercial Kitchen Equipment Service

Coding

Coded - Design and coding required

Number of Pages Required

1 page

Font styles to use
Serif
Sans Serif

Requirements
Must have
• Contact and service request forms, Click-to-call functionality for mobile, Clean, modern layout with strong visuals, Easy navigation, mobile-friendly
Nice to have
• Testimonials or Reviews, If possible a click-to-text functionality for mobile.
Should not have
• Any mention of Refrigeration or HVAC, "Free Quotes"

```html
<!DOCTYPE html>
<html lang="en">
<head>
<meta charset="utf-8">
<title>Hearthline Kitchen Service</title>
<link href="https://fonts.googleapis.com/css2?family=Manrope:wght@300;400;500;600;700;800&display=swap" rel="stylesheet">
<style>
:root{
  --page:#f3f3f3;
  --white:#ffffff;
  --teal:#036a83;
  --teal-dark:#02576c;
  --ink:#111a1f;
  --muted:#6b7378;
  --forest:#0c2b19;
  --form-bg:#d5e7eb;
  --star:#e4cc17;
  --card:#f5f5f5;
}
*{margin:0;padding:0;box-sizing:border-box}
html,body{width:672px;height:1200px;overflow:hidden;background:var(--page)}
body{font-family:'Manrope',sans-serif;color:var(--ink);position:relative}
.desktop,.mobile{position:absolute;background:var(--white);overflow:hidden}
.desktop{left:58px;top:26px;width:432px;height:1124px}
.mobile{left:532px;top:26px;width:71px;height:1115px}
.desktop *,.mobile *{position:absolute;white-space:nowrap}
.wrap{white-space:normal !important}
.icon-sprites{position:absolute;width:0;height:0}
.brand{font-weight:700;color:var(--teal);letter-spacing:.02em}
.brand-box{border:1px solid var(--teal)}
.teal-bg{background:var(--teal)}
.light{color:var(--white)}
.center{text-align:center}
.photo{display:block}
.field{background:var(--white);border-radius:1px;color:#9aa3a7}
.btn-dark{background:var(--forest);color:var(--white);border-radius:20px;font-weight:600}
.btn-teal{background:var(--teal);color:var(--white);font-weight:600}
.btn-white{background:var(--white);color:var(--teal);border-radius:20px;font-weight:600}
.check{color:var(--teal);font-weight:600}
.svc-icon{background:var(--teal);border-radius:2px}
.svc-icon svg{position:static;width:100%;height:100%}
.t-card{background:var(--card);border-radius:4px;box-shadow:0 1px 3px rgba(0,0,0,.05)}
.avatar{background:#dedede;border-radius:50%}
.stars{color:var(--star);letter-spacing:.05em}
</style>
</head>
<body>

<svg class="icon-sprites" aria-hidden="true">
  <defs>
    <symbol id="i-phone" viewBox="0 0 20 20"><circle cx="10" cy="10" r="10" fill="#fff"/><path d="M7 5.5c.6 0 1.2 1.6 1.2 2.1 0 .6-.8.8-.6 1.4.4 1.1 1.4 2.1 2.5 2.5.6.2.8-.6 1.4-.6.5 0 2.1.6 2.1 1.2 0 .9-1 1.9-2 1.8-3.4-.3-6.1-3-6.4-6.4C5.1 6.5 6.1 5.5 7 5.5z" fill="var(--forest)"/></symbol>
    <symbol id="i-wrench" viewBox="0 0 20 20"><path d="M12.5 4a3.5 3.5 0 0 0-3.3 4.6L4.5 13.3l2.2 2.2 4.7-4.7A3.5 3.5 0 0 0 16 7.5l-2 2-2-.5-.5-2 2-2A3.5 3.5 0 0 0 12.5 4z" fill="#fff"/></symbol>
    <symbol id="i-roof" viewBox="0 0 20 20"><path d="M3 14 8 6h9l-3 8zM9 8l-2 4M12 8l-2 4" fill="none" stroke="#fff" stroke-width="1.4" stroke-linejoin="round"/></symbol>
    <symbol id="i-bricks" viewBox="0 0 20 20"><path d="M5 5h5v3H5zM5 9h10v3H5zM5 13h10v3H5z" fill="#fff"/></symbol>
    <symbol id="i-tools" viewBox="0 0 20 20"><path d="M5 5l10 10M15 5 5 15" stroke="#fff" stroke-width="2" stroke-linecap="round"/></symbol>
    <symbol id="i-badge" viewBox="0 0 20 20"><circle cx="10" cy="10" r="8" fill="none" stroke="currentColor" stroke-width="1.2"/><path d="M6.5 10.2 9 12.6 13.6 7.6" fill="none" stroke="currentColor" stroke-width="1.2"/></symbol>
    <symbol id="i-clock" viewBox="0 0 20 20"><circle cx="10" cy="10" r="8" fill="none" stroke="currentColor" stroke-width="1.2"/><path d="M10 5.5V10l3 2" fill="none" stroke="currentColor" stroke-width="1.2"/></symbol>
    <symbol id="i-pin" viewBox="0 0 20 20"><path d="M10 2.5a5.5 5.5 0 0 0-5.5 5.5c0 4 5.5 9.5 5.5 9.5s5.5-5.5 5.5-9.5A5.5 5.5 0 0 0 10 2.5z" fill="none" stroke="currentColor" stroke-width="1.2"/><circle cx="10" cy="8" r="2" fill="none" stroke="currentColor" stroke-width="1.2"/></symbol>
    <symbol id="i-cal" viewBox="0 0 20 20"><rect x="3.5" y="4.5" width="13" height="12" rx="1.5" fill="none" stroke="currentColor" stroke-width="1.2"/><path d="M3.5 8h13M7 3v3M13 3v3" stroke="currentColor" stroke-width="1.2"/></symbol>
    <symbol id="i-award" viewBox="0 0 20 20"><circle cx="10" cy="8" r="5.5" fill="none" stroke="#fff" stroke-width="1.5"/><path d="M6.5 12 4.5 18l3-1.5L9 18.5M13.5 12l2 6-3-1.5L11 18.5" fill="none" stroke="#fff" stroke-width="1.3"/><path d="M8 8l1.5 1.5L12.5 6.5" fill="none" stroke="#fff" stroke-width="1.3"/></symbol>
    <symbol id="i-doc" viewBox="0 0 20 20"><path d="M5 2.5h7l3 3v12H5z" fill="none" stroke="#fff" stroke-width="1.5"/><path d="M7.5 8h5M7.5 11h5M7.5 14h3" stroke="#fff" stroke-width="1.3"/></symbol>
    <symbol id="i-24" viewBox="0 0 20 20"><circle cx="10" cy="10" r="8" fill="none" stroke="#fff" stroke-width="1.5"/><circle cx="10" cy="10" r="4.5" fill="#fff"/><path d="M8 9.2h1.6L8 11h1.8M11 8.8v2.2h1.4M12 8.8v3" fill="none" stroke="var(--teal)" stroke-width=".7"/></symbol>
    <symbol id="i-chat" viewBox="0 0 20 20"><path d="M3 4h10v7H7l-3 2.5V11H3z" fill="#fff"/><path d="M9 12.5h4.5l3 2.5V12H17V7h-2" fill="none" stroke="#fff" stroke-width="1.3"/></symbol>
    <symbol id="i-social" viewBox="0 0 10 10"><rect x="1" y="1" width="8" height="8" rx="2" fill="currentColor"/></symbol>
  </defs>
</svg>

<main class="desktop">

  <header class="site-nav">
    <div class="brand brand-box" style="left:37px;top:7px;height:12px;padding:0 3px;font-size:6.3px;line-height:11px">HEARTHLINE</div>
    <span style="left:170px;top:10px;font-size:4px;font-weight:500">About Us</span>
    <span style="left:201px;top:10px;font-size:4px;font-weight:500">Services</span>
    <span style="left:231px;top:10px;font-size:4px;font-weight:500">Our Blog</span>
    <span style="left:261px;top:10px;font-size:4px;font-weight:500">Contact</span>
    <span style="left:358px;top:11.5px;width:2.4px;height:2.4px;border-radius:50%;background:#e2443b"></span>
    <span style="left:363px;top:10px;font-size:4px;font-weight:500">24 Hour Services</span>
  </header>

  <section class="hero">
    <div class="teal-bg" style="left:0;top:26.5px;width:432px;height:183.5px"></div>
    <svg style="left:96px;top:209px;width:239px;height:12px" viewBox="0 0 239 12"><path d="M0 0h239l-11 11H11z" fill="var(--teal)"/></svg>
    <div class="photo" role="img" aria-label="Cast iron skillet hanging in a kitchen" style="left:4px;top:26.5px;width:92px;height:179px;background:radial-gradient(circle at 45% 45%,#3a3f4b 0,#1c1f26 40%,#2a4d8a 75%,#6d8ed0 100%)"></div>
    <div class="photo" role="img" aria-label="Stainless stove knobs with copper pots in the background" style="left:335px;top:26.5px;width:93px;height:179px;background:linear-gradient(160deg,#c9c6c0 0,#8b8a8d 30%,#3f475e 60%,#1f2638 100%);border-radius:0 0 4px 0"></div>

    <div class="light center" style="left:96px;width:239px;top:63px;font-size:4.4px;font-weight:500">Maintenances&nbsp;&nbsp;•&nbsp;&nbsp;Repairs&nbsp;&nbsp;•&nbsp;&nbsp;Improvements</div>
    <h1 class="light center wrap" style="left:96px;width:239px;top:74px;font-size:15.6px;line-height:17px;font-weight:700;letter-spacing:-.01em">Need to improve or repair your equipment? We can help!</h1>
    <div class="light center" style="left:96px;width:239px;top:115px;font-size:4.6px">✓ Fast Response&nbsp;&nbsp;&nbsp;&nbsp;&nbsp;✓ 100% Commitment-Free</div>
    <div class="btn-dark" style="left:189px;top:132px;width:53px;height:15px;font-size:5.2px;line-height:15px;padding-left:6px">Call Us Now</div>
    <svg style="left:231px;top:135px;width:9px;height:9px"><use href="#i-phone"/></svg>

    <div class="hero-features light" style="left:115px;top:167px;width:200px;height:12px;font-size:4px;line-height:5px;color:#fff">
      <svg style="left:0;top:1px;width:9px;height:9px;color:#fff"><use href="#i-badge"/></svg>
      <span style="left:14px;top:0">Satisfaction<br>Guarantee</span>
      <svg style="left:53px;top:1px;width:9px;height:9px;color:#fff"><use href="#i-clock"/></svg>
      <span style="left:67px;top:0">24H<br>Availability</span>
      <svg style="left:103px;top:1px;width:9px;height:9px;color:#fff"><use href="#i-pin"/></svg>
      <span style="left:117px;top:0">Local<br>Professional</span>
      <svg style="left:156px;top:1px;width:9px;height:9px;color:#fff"><use href="#i-cal"/></svg>
      <span style="left:170px;top:0">Flexible<br>Appointments</span>
    </div>
  </section>

  <section class="experts">
    <h2 style="left:54px;top:246px;font-size:12px;line-height:14.5px;font-weight:600">Your Kitchen<br>Equipment Experts</h2>
    <p class="wrap" style="left:54px;top:280px;width:135px;font-size:3.8px;line-height:6.3px;color:var(--muted)">We specialize in restaurant equipment services across the US. Our comprehensive solutions ensure your kitchen operates at its best.</p>
    <span class="check" style="left:54px;top:305px;font-size:4.3px">✓&nbsp; Repair and Installation</span>
    <span class="check" style="left:121px;top:305px;font-size:4.3px">✓&nbsp; Inspections</span>
    <span class="check" style="left:54px;top:318.5px;font-size:4.3px">✓&nbsp; Maintenance</span>
    <span class="check" style="left:121px;top:318.5px;font-size:4.3px">✓&nbsp; Cost-Effective</span>
    <span class="check" style="left:54px;top:332px;font-size:4.3px">✓&nbsp; Equipment Servicing</span>
    <span class="check" style="left:121px;top:332px;font-size:4.3px">✓&nbsp; Energy-efficient solutions</span>
    <div class="teal-bg light wrap" style="left:54px;top:351px;width:101px;height:17px;border-radius:4px;font-size:3.9px;line-height:6px;padding:3px 7px">We're available 24/7 for fast service. Contact us at (888) 555-0142</div>

    <form class="request-form" style="left:248px;top:234px;width:125px;height:152px;background:var(--form-bg);border-radius:3px">
      <span style="left:9px;top:12.5px;font-size:4.4px;font-weight:600">Pick The Services You Want</span>
      <div class="field" style="left:9px;top:26px;width:108px;height:18px;font-size:3.2px;line-height:18px;padding-left:7px">Full Name</div>
      <div class="field" style="left:9px;top:49px;width:108px;height:17px;font-size:3.2px;line-height:17px;padding-left:7px">Email address</div>
      <div class="field" style="left:9px;top:72px;width:108px;height:17px;font-size:3.2px;line-height:17px;padding-left:7px">Phone</div>
      <div class="field" style="left:9px;top:95px;width:108px;height:17px;font-size:3.2px;line-height:17px;padding-left:7px">Services type</div>
      <svg style="left:107px;top:102px;width:4px;height:3px" viewBox="0 0 8 5"><path d="M1 1l3 3 3-3" fill="none" stroke="#666" stroke-width="1"/></svg>
      <div class="btn-teal center" style="left:9px;top:120px;width:108px;height:23px;border-radius:2px;font-size:4.6px;line-height:23px;background:var(--teal-dark)">Get Schedule</div>
    </form>
    <div class="photo" role="img" aria-label="Vintage kitchen weighing scale" style="left:358px;top:337px;width:40px;height:54px;border-radius:40% 40% 10px 10px;background:radial-gradient(circle at 50% 62%,#f4f4f4 0,#d8d8d8 35%,#8d8f92 60%,#3d3f43 100%)"></div>
  </section>

  <section class="services">
    <h2 class="center" style="left:0;width:432px;top:405px;font-size:12px;font-weight:600">Our Services</h2>
    <p class="center wrap" style="left:141px;width:150px;top:425px;font-size:3.8px;line-height:6.3px;color:var(--muted)">From ovens to fryers, we've got your essential kitchen equipment covered!</p>

    <div class="svc-icon" style="left:61px;top:452px;width:14px;height:14px"><svg><use href="#i-wrench"/></svg></div>
    <span style="left:61px;top:470px;font-size:5.2px;font-weight:600">Oven repair</span>
    <p class="wrap" style="left:61px;top:480px;width:68px;font-size:3.8px;line-height:6.3px;color:var(--muted)">Gas and electric oven repair, calibration, and maintenance</p>

    <div class="svc-icon" style="left:142px;top:452px;width:14px;height:14px"><svg><use href="#i-roof"/></svg></div>
    <span style="left:142px;top:470px;font-size:5.2px;font-weight:600">Fryer maintenance</span>
    <p class="wrap" style="left:142px;top:480px;width:70px;font-size:3.8px;line-height:6.3px;color:var(--muted)">Deep fryer repair, cleaning, and oil filtration system service</p>

    <div class="svc-icon" style="left:223px;top:452px;width:14px;height:14px"><svg><use href="#i-bricks"/></svg></div>
    <span style="left:223px;top:470px;font-size:5.2px;font-weight:600">Cooking Utensil</span>
    <p class="wrap" style="left:223px;top:480px;width:70px;font-size:3.8px;line-height:6.3px;color:var(--muted)">Mixers, processors, and specialty cooking tools repair</p>

    <div class="svc-icon" style="left:304px;top:452px;width:14px;height:14px"><svg><use href="#i-tools"/></svg></div>
    <span style="left:304px;top:470px;font-size:5.2px;font-weight:600">Dishwasher repair</span>
    <p class="wrap" style="left:304px;top:480px;width:68px;font-size:3.8px;line-height:6.3px;color:var(--muted)">Commercial dishwasher, conveyor, and sanitization system service</p>

    <div class="teal-bg" style="left:142px;top:513px;width:148px;height:39px;border-radius:4px">
      <span class="light" style="left:7px;top:6.5px;font-size:5px;font-weight:600">More service?</span>
      <p class="light wrap" style="left:7px;top:14.5px;width:70px;font-size:3.8px;line-height:6.3px">Let us know how we can help keep your kitchen running smoothly!</p>
      <div class="btn-white center" style="left:78px;top:13px;width:63px;height:13.5px;font-size:5px;line-height:13.5px">Call Us Now</div>
    </div>
  </section>

  <section class="promise teal-bg" style="left:14px;top:570px;width:405px;height:135px;border-radius:5px">
    <h2 class="light wrap" style="left:40px;top:14px;width:130px;font-size:11.6px;line-height:14.5px;font-weight:600">Rapid, Reliable, and Guaranteed Service</h2>
    <p class="light wrap" style="left:226px;top:15px;width:142px;font-size:5.4px;line-height:6.3px">We're dedicated to keeping your restaurant equipment in top shape, ensuring minimal downtime and maximum efficiency.</p>
    <div style="left:40px;top:50px;width:326px;height:.5px;background:rgba(255,255,255,.25)"></div>

    <svg style="left:43px;top:57px;width:18px;height:18px"><use href="#i-award"/></svg>
    <span class="light" style="left:70px;top:57.5px;font-size:5.2px;font-weight:600">Satisfaction Guarantee</span>
    <p class="light wrap" style="left:70px;top:66px;width:116px;font-size:3.8px;line-height:6.3px">Rest assured, our certified technicians deliver top-quality service and lasting solutions.</p>

    <svg style="left:226px;top:57px;width:18px;height:18px"><use href="#i-doc"/></svg>
    <span class="light" style="left:252px;top:57.5px;font-size:5.2px;font-weight:600">Clear Estimates</span>
    <p class="light wrap" style="left:252px;top:66px;width:110px;font-size:3.8px;line-height:6.3px">Get no-obligation estimates tailored to your specific equipment needs. Experience transparent pricing and reliable service.</p>

    <svg style="left:42px;top:99px;width:20px;height:20px"><use href="#i-24"/></svg>
    <span class="light" style="left:70px;top:99.5px;font-size:5.2px;font-weight:600">24/7 Emergency Service</span>
    <p class="light wrap" style="left:70px;top:108px;width:118px;font-size:3.8px;line-height:6.3px">Unexpected equipment failure? Our expert technicians are ready to provide immediate assistance, day or night.</p>

    <svg style="left:224px;top:99px;width:20px;height:20px"><use href="#i-chat"/></svg>
    <span class="light" style="left:252px;top:99.5px;font-size:5.2px;font-weight:600">100% Commitment-Free</span>
    <p class="light wrap" style="left:252px;top:108px;width:112px;font-size:3.8px;line-height:6.3px">Discuss your equipment concerns with us. We offer expert advice with no strings attached.</p>
  </section>

  <section class="testimonials">
    <span style="left:25px;top:728px;width:6px;height:6px;border-radius:50%;background:#9cc4ea"></span>
    <span style="left:26.5px;top:729.5px;width:3px;height:3px;border-radius:50%;background:#1f73c9"></span>
    <span style="left:37px;top:727px;font-size:6.6px;font-weight:500;color:var(--teal)">Partner in Kitchen Services</span>
    <h2 style="left:25px;top:737px;font-size:20px;font-weight:400;color:var(--forest);letter-spacing:-.01em">Costumer Testimonials</h2>
    <p class="wrap" style="left:249px;top:739px;width:160px;font-size:7.6px;line-height:7.9px;color:var(--muted)">Delivering expert kitchen solutions from quick repairs to installations, our team provides lasting quality</p>

    <article class="t-card" style="left:25px;top:778px;width:123px;height:77px">
      <span class="avatar" style="left:11px;top:7.5px;width:15px;height:15px"></span>
      <span style="left:32px;top:10px;font-size:5.6px;font-weight:500">Owen Carter</span>
      <span style="left:32px;top:20px;font-size:3.8px;color:var(--muted)">Restaurant Owner</span>
      <p class="wrap" style="left:11px;top:34px;width:104px;font-size:3.3px;line-height:6.3px;color:var(--muted)">Hearthline has helped me find a steady service partner. I used to struggle with finding reliable repair help but the team guides us well</p>
      <span class="stars" style="left:11px;top:59px;font-size:8px">★★★★★</span>
    </article>
    <article class="t-card" style="left:161px;top:778px;width:122px;height:77px">
      <span class="avatar" style="left:11px;top:7.5px;width:15px;height:15px"></span>
      <span style="left:33px;top:10px;font-size:5.6px;font-weight:500">Lena Brooks</span>
      <span style="left:33px;top:20px;font-size:3.8px;color:var(--muted)">Kitchen Manager</span>
      <p class="wrap" style="left:11px;top:34px;width:104px;font-size:3.3px;line-height:6.3px;color:var(--muted)">Hearthline has helped me find a steady service partner. I used to struggle with finding reliable repair help but the team guides us well</p>
      <span class="stars" style="left:11px;top:59px;font-size:8px">★★★★★</span>
    </article>
    <article class="t-card" style="left:296px;top:778px;width:122px;height:77px">
      <span class="avatar" style="left:11px;top:7.5px;width:15px;height:15px"></span>
      <span style="left:32px;top:10px;font-size:5.6px;font-weight:500">Marco Ruiz</span>
      <span style="left:32px;top:20px;font-size:3.8px;color:var(--muted)">Head Chef</span>
      <p class="wrap" style="left:11px;top:34px;width:104px;font-size:3.3px;line-height:6.3px;color:var(--muted)">Hearthline has helped me find a steady service partner. I used to struggle with finding reliable repair help but the team guides us well</p>
      <span class="stars" style="left:11px;top:59px;font-size:8px">★★★★★</span>
    </article>
  </section>

  <section class="closing-cta">
    <h2 class="wrap" style="left:40px;top:912px;width:180px;font-size:14.4px;line-height:16.7px;font-weight:700">Ready to optimize your kitchen's performance? Let’s Talk!</h2>
    <span class="check" style="left:40px;top:969.5px;font-size:4.6px;font-weight:500">✓ Fast Response&nbsp;&nbsp;&nbsp;&nbsp;✓ 100% Commitment-Free</span>
    <div class="btn-teal" style="left:40px;top:983px;width:52px;height:14.5px;border-radius:10px;font-size:5.6px;line-height:14.5px;padding-left:5.5px">Call Us Now</div>
    <div class="photo" role="img" aria-label="White countertop appliances: coffee maker, blender, kettle, hand mixer and toaster" style="left:221px;top:863px;width:200px;height:149px;background:radial-gradient(ellipse at 50% 55%,#f2f2f2 0,#e2e2e4 45%,#ffffff 75%)"></div>
  </section>

  <footer class="site-footer teal-bg" style="left:0;top:1021px;width:432px;height:103px">
    <div class="brand" style="left:54px;top:16px;width:54px;height:16px;background:#fff;font-size:6.3px;line-height:16px;text-align:center">HEARTHLINE</div>
    <p class="light wrap" style="left:54px;top:40px;width:100px;font-size:3.9px;line-height:6.3px">Hearthline is the leading provider for restaurant cooking equipment service and repair.</p>
    <div style="left:54px;top:60px;height:5px;width:50px;color:#fff">
      <svg style="left:0;width:5px;height:5px"><use href="#i-social"/></svg>
      <svg style="left:11px;width:5px;height:5px"><use href="#i-social"/></svg>
      <svg style="left:22px;width:5px;height:5px"><use href="#i-social"/></svg>
      <svg style="left:33px;width:5px;height:5px"><use href="#i-social"/></svg>
      <svg style="left:44px;width:5px;height:5px"><use href="#i-social"/></svg>
    </div>
    <span class="light" style="left:311px;top:16.5px;font-size:5.6px;font-weight:600">Company</span>
    <span class="light" style="left:360px;top:16.5px;font-size:5.6px;font-weight:600">Legal</span>
    <span class="light" style="left:311px;top:29.5px;font-size:4.4px">About us</span>
    <span class="light" style="left:311px;top:39.5px;font-size:4.4px">Services</span>
    <span class="light" style="left:311px;top:49.5px;font-size:4.4px">Our Blog</span>
    <span class="light" style="left:311px;top:59.5px;font-size:4.4px">Contact</span>
    <span class="light" style="left:360px;top:29.5px;font-size:4.4px">Terms</span>
    <span class="light" style="left:360px;top:39.5px;font-size:4.4px">Privacy</span>
    <span class="light" style="left:360px;top:49.5px;font-size:4.4px">Cookies</span>
    <span class="light" style="left:360px;top:59.5px;font-size:4.4px">License</span>
    <div style="left:0;top:82px;width:432px;height:.5px;background:rgba(255,255,255,.25)"></div>
    <span class="light center" style="left:0;width:432px;top:90px;font-size:3.9px">©2023 Hearthline. All rights reserved</span>
  </footer>
</main>

<main class="mobile">
  <div class="brand brand-box" style="left:6px;top:3.5px;height:6.5px;padding:0 1.5px;font-size:3.2px;line-height:5.5px">HEARTHLINE</div>
  <svg style="left:65px;top:5px;width:4px;height:3.5px" viewBox="0 0 8 7"><path d="M0 1h8M0 3.5h8M0 6h8" stroke="var(--teal)" stroke-width="1"/></svg>

  <div class="teal-bg" style="left:0;top:14px;width:71px;height:100px"></div>
  <svg style="left:0;top:113px;width:71px;height:8px" viewBox="0 0 71 8"><path d="M0 0h71l-9 7H9z" fill="var(--teal)"/></svg>
  <span class="light" style="left:0;top:16px;font-size:1.9px;opacity:.85">Kitchen Appliance&nbsp; •&nbsp; Kitchen Repairs&nbsp; •&nbsp; Kitchen Upgrades</span>
  <h1 class="light center wrap" style="left:5px;width:61px;top:22.5px;font-size:6.3px;line-height:7.5px;font-weight:600">Need to repair or upgrade your kitchen? We can help!</h1>
  <span class="light center" style="left:0;width:71px;top:58px;font-size:2.1px;opacity:.85">✓ Fast Response&nbsp;&nbsp; ✓ 100% Commitment-Free</span>
  <div class="center" style="left:19px;top:65px;width:33px;height:9px;border-radius:5px;background:#17a9e0;color:#fff;font-size:2.7px;line-height:9px;font-weight:600;padding-right:6px">Call Us Now</div>
  <svg style="left:45.5px;top:67px;width:5px;height:5px"><use href="#i-phone"/></svg>

  <div style="left:35px;top:79px;width:.3px;height:33px;background:rgba(255,255,255,.25)"></div>
  <svg style="left:16px;top:78px;width:3.5px;height:3.5px;color:#fff"><use href="#i-clock"/></svg>
  <span class="light center" style="left:0;width:36px;top:83px;font-size:2.1px;line-height:2.8px">Satisfaction<br>Guarantee</span>
  <svg style="left:51.5px;top:78px;width:3.5px;height:3.5px;color:#fff"><use href="#i-clock"/></svg>
  <span class="light center" style="left:36px;width:35px;top:83px;font-size:2.1px;line-height:2.8px">24H<br>Availability</span>
  <svg style="left:16px;top:100px;width:3.5px;height:3.5px;color:#fff"><use href="#i-pin"/></svg>
  <span class="light center" style="left:0;width:36px;top:105px;font-size:2.1px;line-height:2.8px">Local US<br>Professional</span>
  <svg style="left:51.5px;top:100px;width:3.5px;height:3.5px;color:#fff"><use href="#i-cal"/></svg>
  <span class="light center" style="left:36px;width:35px;top:105px;font-size:2.1px;line-height:2.8px">Flexible<br>Appointments</span>

  <h2 class="wrap" style="left:2px;top:131px;width:50px;font-size:4.2px;line-height:6px;font-weight:700">Professional kitchen services</h2>
  <p class="wrap" style="left:2px;top:146px;width:66px;font-size:2.4px;line-height:5.2px;color:var(--muted)">Need help with your kitchen? We are kitchen care professionals focused in the US region. We provide several services that support kitchen services</p>

  <div style="left:2px;top:173px;width:67px;height:87px;background:var(--form-bg);border-radius:2px">
    <span style="left:5px;top:7px;font-size:2.8px;font-weight:600">Pick The Services You Want</span>
    <div class="field" style="left:4px;top:15px;width:59px;height:9.5px;font-size:1.9px;line-height:9.5px;padding-left:4px">Full Name</div>
    <div class="field" style="left:4px;top:28px;width:59px;height:10px;font-size:1.9px;line-height:10px;padding-left:4px">Email address</div>
    <div class="field" style="left:4px;top:41px;width:59px;height:10px;font-size:1.9px;line-height:10px;padding-left:4px">Phone</div>
    <div class="field" style="left:4px;top:54px;width:59px;height:10px;font-size:1.9px;line-height:10px;padding-left:4px">Services type</div>
    <div class="btn-teal center" style="left:4px;top:69px;width:59px;height:13px;border-radius:1px;font-size:3px;line-height:13px;background:var(--teal-dark)">Get Schedule</div>
  </div>

  <span class="check" style="left:2px;top:267.5px;font-size:2.5px">✓&nbsp; Repair and Installation</span>
  <span class="check" style="left:2px;top:276.5px;font-size:2.5px">✓&nbsp; Maintenance</span>
  <span class="check" style="left:2px;top:285.5px;font-size:2.5px">✓&nbsp; Kitchen Safety Services</span>
  <span class="check" style="left:2px;top:294.5px;font-size:2.5px">✓&nbsp; Plumbing</span>
  <span class="check" style="left:2px;top:303.5px;font-size:2.5px">✓&nbsp; Budget-friendly</span>
  <span class="check" style="left:2px;top:312.5px;font-size:2.5px">✓&nbsp; Eco-friendly solutions</span>
  <div class="teal-bg light wrap" style="left:2px;top:322px;width:62px;height:20px;border-radius:2px;font-size:2.4px;line-height:5.2px;padding:2px 4.5px">We are available 24/7 to help you. Contact us at (888) 555-0177</div>

  <h2 class="center" style="left:0;width:71px;top:359.5px;font-size:3.9px;font-weight:600">Our Services</h2>
  <p class="center wrap" style="left:5px;width:61px;top:366.5px;font-size:2.4px;line-height:5.2px;color:var(--muted)">Do you have problems with leaking pipes, broken appliances, or want to remodel your kitchen? We can help!</p>

  <div class="svc-icon" style="left:29.5px;top:389px;width:12px;height:11px"><svg><use href="#i-wrench"/></svg></div>
  <span class="center" style="left:0;width:71px;top:404.5px;font-size:3.9px;font-weight:600">Plumbing services</span>
  <p class="center wrap" style="left:8px;width:55px;top:412.5px;font-size:2.4px;line-height:5.2px;color:var(--muted)">Drain pipe leaking, pipe clogged, replace the pipe line</p>

  <div class="svc-icon" style="left:29.5px;top:429px;width:12px;height:11px"><svg><use href="#i-roof"/></svg></div>
  <span class="center" style="left:0;width:71px;top:444.5px;font-size:3.9px;font-weight:600">Appliance repair</span>
  <p class="center wrap" style="left:7px;width:57px;top:452.5px;font-size:2.4px;line-height:5.2px;color:var(--muted)">Oven not heating, mixer not spinning, dishwasher not cleaning</p>

  <div class="svc-icon" style="left:29.5px;top:469px;width:12px;height:11px"><svg><use href="#i-bricks"/></svg></div>
  <span class="center" style="left:0;width:71px;top:484.5px;font-size:3.9px;font-weight:600">Mold Removal</span>
  <p class="center wrap" style="left:8px;width:55px;top:492.5px;font-size:2.4px;line-height:5.2px;color:var(--muted)">Removing and cleaning mildew, Restoration and Prevention</p>

  <div class="svc-icon" style="left:29.5px;top:509px;width:12px;height:11px"><svg><use href="#i-tools"/></svg></div>
  <span class="center" style="left:0;width:71px;top:524.5px;font-size:3.9px;font-weight:600">Electrical Repair</span>
  <p class="center" style="left:0;width:71px;top:533px;font-size:2.4px;color:var(--muted)">Wiring, outlets, and lighting repair</p>

  <div class="teal-bg" style="left:5px;top:544px;width:62px;height:45px;border-radius:3px">
    <span class="light center" style="left:0;width:62px;top:6.5px;font-size:3.9px;font-weight:600">More service?</span>
    <p class="light center wrap" style="left:6px;width:50px;top:12.5px;font-size:2.4px;line-height:5.2px">Let us know what you need, and we can help!</p>
    <div class="btn-white center" style="left:6px;top:29px;width:50px;height:9px;font-size:2.6px;line-height:9px">Call Us Now</div>
  </div>

  <div class="teal-bg" style="left:5px;top:598px;width:62px;height:301px;border-radius:2px">
    <h3 class="light center wrap" style="left:4px;width:54px;top:7px;font-size:4.1px;line-height:6px;font-weight:600">Fast, Friendly, and Satisfaction Guarantee</h3>
    <p class="light center wrap" style="left:6px;width:50px;top:27px;font-size:2.4px;line-height:5.2px">No matter how big or small your work is, we are ready to serve and help you solve your kitchen problems.</p>

    <svg style="left:24px;top:58px;width:14px;height:14px"><use href="#i-award"/></svg>
    <span class="light center" style="left:0;width:62px;top:76px;font-size:2.6px;font-weight:600">Satisfaction Guarantee</span>
    <p class="light center wrap" style="left:4px;width:54px;top:83px;font-size:2.4px;line-height:5.2px">You don't need to worry about scams or our performance results. Our company has been verified and strives for optimal results</p>

    <svg style="left:24px;top:118px;width:14px;height:14px"><use href="#i-doc"/></svg>
    <span class="light center" style="left:0;width:62px;top:136px;font-size:2.6px;font-weight:600">Clear Estimates</span>
    <p class="light center wrap" style="left:7px;width:48px;top:143px;font-size:2.4px;line-height:5.2px">Get personalized cost estimates without any obligation. Experience transparency and peace of mind as you explore our service.</p>

    <svg style="left:24px;top:184px;width:14px;height:14px"><use href="#i-24"/></svg>
    <span class="light center" style="left:0;width:62px;top:202px;font-size:2.6px;font-weight:600">Fast 24-Hour Service</span>
    <p class="light center wrap" style="left:6px;width:50px;top:209px;font-size:2.4px;line-height:5.2px">Need fast handling for repairs to drains, leaks, or something else? Our experts are available anytime to help you solve the problem</p>

    <svg style="left:24px;top:246px;width:14px;height:14px"><use href="#i-chat"/></svg>
    <span class="light center" style="left:0;width:62px;top:262px;font-size:2.6px;font-weight:600">Expertise and Experience</span>
    <p class="light center wrap" style="left:5px;width:52px;top:269px;font-size:2.4px;line-height:5.2px">You are free to ask us about the problems you are facing. We offer a no-commitment approach to put your mind at ease</p>
  </div>

  <h2 class="center wrap" style="left:8px;width:55px;top:916.5px;font-size:3.9px;line-height:6px;font-weight:600">Ready to improve or repair your kitchen? Let’s Talk!</h2>
  <span class="check center" style="left:0;width:71px;top:939.5px;font-size:2.1px;font-weight:500">✓ Fast Response&nbsp;&nbsp; ✓ 100% Commitment-Free</span>
  <div class="btn-teal center" style="left:19px;top:948px;width:33px;height:9px;border-radius:5px;font-size:2.7px;line-height:9px;padding-right:6px">Call Us Now</div>
  <svg style="left:45.5px;top:950px;width:5px;height:5px"><use href="#i-phone"/></svg>
  <div class="photo" role="img" aria-label="White countertop appliances group" style="left:8px;top:959px;width:53px;height:30px;background:radial-gradient(ellipse at 50% 55%,#ececee 0,#dedee0 45%,#ffffff 80%)"></div>

  <footer class="teal-bg" style="left:0;top:1002px;width:71px;height:113px">
    <div class="brand" style="left:5px;top:7px;width:45px;height:12px;background:#fff;font-size:4.2px;line-height:12px;text-align:center">HEARTHLINE</div>
    <p class="light wrap" style="left:5px;top:28px;width:60px;font-size:2.4px;line-height:5.2px">Hearthline is your premier destination for top-notch kitchen service and repair.</p>
    <div style="left:5px;top:48.5px;height:4px;width:40px;color:#fff">
      <svg style="left:0;width:3.5px;height:3.5px"><use href="#i-social"/></svg>
      <svg style="left:9px;width:3.5px;height:3.5px"><use href="#i-social"/></svg>
      <svg style="left:18px;width:3.5px;height:3.5px"><use href="#i-social"/></svg>
      <svg style="left:27px;width:3.5px;height:3.5px"><use href="#i-social"/></svg>
      <svg style="left:36px;width:3.5px;height:3.5px"><use href="#i-social"/></svg>
    </div>
    <span class="light" style="left:5px;top:59px;font-size:3.6px;font-weight:600">Company</span>
    <span class="light" style="left:39px;top:59px;font-size:3.6px;font-weight:600">Legal</span>
    <span class="light" style="left:5px;top:69.5px;font-size:2.6px">About us</span>
    <span class="light" style="left:5px;top:78px;font-size:2.6px">Services</span>
    <span class="light" style="left:5px;top:86.5px;font-size:2.6px">Our Blog</span>
    <span class="light" style="left:5px;top:94.5px;font-size:2.6px">Contact</span>
    <span class="light" style="left:39px;top:69.5px;font-size:2.6px">Terms</span>
    <span class="light" style="left:39px;top:78px;font-size:2.6px">Privacy</span>
    <span class="light" style="left:39px;top:86.5px;font-size:2.6px">Cookies</span>
    <span class="light" style="left:39px;top:94.5px;font-size:2.6px">License</span>
    <div style="left:0;top:105px;width:71px;height:.3px;background:rgba(255,255,255,.3)"></div>
    <span class="light center" style="left:0;width:71px;top:108.5px;font-size:2.4px">©2023 Hearthline. All rights reserved</span>
  </footer>
</main>

</body>
</html>
```